Book Cover

Book Title: THE QUIET LEDGER
Book Sub Title: Notes on slowing the daily rush and shaping a calmer household rhythm
Vibe: Professional, stylish, trustworthy (high-end men's fashion)
Website (for inspiration): www.brindlequarry.com
Attached: a potential photo to use for the cover, but open to other options (from our website)

```html
<!DOCTYPE html>
<html lang="en">
<head>
<meta charset="utf-8">
<title>The Quiet Ledger — Book Cover</title>
<link rel="stylesheet" href="https://fonts.googleapis.com/css2?family=Archivo+Black&family=Oswald:wght@400&family=Pinyon+Script&display=swap">
<style>
  :root {
    --backdrop: #b5c3c1;
    --cover: #0b1114;
    --gold: #c2a56c;
    --white: #ffffff;
    --loft-light: #e8e1d0;
    --loft-mid: #cbbd9f;
    --loft-dark: #9a8a6c;
    --floor: #b9a58a;
  }
  html, body {
    margin: 0;
    padding: 0;
    width: 910px;
    height: 1200px;
    overflow: hidden;
    background: var(--backdrop);
  }
  .canvas {
    position: relative;
    width: 910px;
    height: 1200px;
    background: var(--backdrop);
  }
  .cover {
    position: absolute;
    left: 128px;
    top: 134px;
    width: 668px;
    height: 933px;
    background: var(--cover);
  }
  .title-art {
    position: absolute;
    left: 0;
    top: 0;
    width: 668px;
    height: 600px;
  }
  .title-art text {
    font-family: "Archivo Black", "Arial Black", sans-serif;
    font-size: 150px;
  }
  .subtitle {
    position: absolute;
    left: 79px;
    top: 836px;
    margin: 0;
    font-family: "Oswald", "Arial Narrow", sans-serif;
    font-weight: 400;
    font-size: 22px;
    line-height: 30px;
    letter-spacing: 0.4px;
    text-transform: uppercase;
    color: var(--gold);
  }
  .subtitle .initial {
    font-family: "Pinyon Script", cursive;
    text-transform: none;
    color: var(--white);
    font-size: 84px;
    line-height: 0;
    vertical-align: -2px;
    margin-right: 2px;
  }
  .subtitle .line { display: block; }
  .accent-rule {
    position: absolute;
    left: 431px;
    top: 826px;
    width: 106px;
    height: 5px;
    background: var(--white);
  }
</style>
</head>
<body>
  <main class="canvas">
    <section class="cover">
      <svg class="title-art" viewBox="0 0 668 600" role="img" aria-label="Book title THE QUIET LEDGER in heavy letters, filled with a photograph of a man in a navy suit seated on a wooden stool beside a clothing rail in a sunlit brick loft">
        <defs>
          <linearGradient id="loftTones" x1="0" y1="0" x2="0.3" y2="1">
            <stop offset="0" stop-color="var(--loft-mid)"/>
            <stop offset="0.3" stop-color="var(--loft-light)"/>
            <stop offset="0.55" stop-color="var(--loft-dark)"/>
            <stop offset="0.7" stop-color="var(--loft-light)"/>
            <stop offset="1" stop-color="var(--floor)"/>
          </linearGradient>
        </defs>
        <g fill="url(#loftTones)" transform="translate(0,0) scale(1,1.3)">
          <text x="67" y="198" textLength="380" lengthAdjust="spacingAndGlyphs">THE</text>
          <text x="67" y="318" textLength="540" lengthAdjust="spacingAndGlyphs">QUIET</text>
          <text x="67" y="438" textLength="540" lengthAdjust="spacingAndGlyphs">LEDGER</text>
        </g>
      </svg>

      <p class="subtitle">
        <span class="line"><span class="initial">N</span>otes on slowing the</span>
        <span class="line">daily rush and shaping a</span>
        <span class="line">calmer household rhythm</span>
      </p>

      <div class="accent-rule"></div>
    </section>
  </main>
</body>
</html>
```